Web-page design

We need a initial web design for our page kelbrook.com.au (which is not yet set up).
We provide consulting services for all kinds of problems in and between organisations.
Main focus is on conflict resolution but we also support companies on improving their operational performance.
We want to have the following page structure (and part of the project is to design the 8 pages):
- Home
- Services (we offer 3 main service areas - one per page)
- Case studies (one per page)
- Engaging us (our process)
- About Conflict & low performance
- Conflict resolution App
- About
- Contact (Email form)
- Our logo should be on each page.
The start page should include the following information:
- Twitter / Linkedin / facebook/ google + Links
- Telephone / Email or in general contact details
- News
- A quite prominent picture box with 3 alternating pics - each representing one of our service areas
- Link to our App
- Testimonials
It would be nice if the service pages would have an image header. Links to the information section (about conflict & low performance; and the app page) would be nice as well.
We like the following joomla designs: www.frandelthemes.com/itempreview/153
No need to copy it, it should just give you an idea.
We like the layout here with the picture and space for the case studies on the left. Somewhere beneath should be the 3 service areas with a picture each.
In terms of colors: our logo colours are Blue (RBG 8;44;80) and Orange (RGB 231;120;23). The orange could be used to emphasise certain things, however there should not be too much color.
Budget for images available, so please use placeholders or ask us for specific photos/images, if you need them for your design.
Updates
Hi, one more thing that we would like to have is the case studies not hidden behind a link "case studies" - we would like to have them individually linked prominent on the first page. There will be about 6-8 of them. Thats what we liked on the joomla template (the links left from the picture).
Hi, thanks very much for all the great proposals.
We are currently going through the selection process and will post our decision early next week.
Thanks again!
Wilma
Target Market(s)
- target customers are all different kinds of businesses and organisations (all industries, government, non-for-profit, ...) experiencing conflict and tension - be it with internal staff, amongst managers or board members, dysfunctional teams, between organizations or customers and organizations... examples could be bullying allegations, governmental negotiations with unions, disputes within organizations etc.
- also we will offer performance improvement services for organizations
- we will offer mediation, facilitation, negotiation, performance improvement services, conflict coaching, conflict management, change management services
- if comparable to anything - then to a law firm in terms of dealing with conflicts but its much less adversarial and much more about the people and their interests rather than about laws
- basically it's all kind of things you can do in order to solve disputes without involving lawyers and a court - so it's much cheaper and target is to find a solution all parties can live with rather than having a judge deciding about who wins and who looses
- performance management is more about analysing reasons for a lack of performance and setting up continous improvement systems, supporting change management, facilitating improvement workshops or strategic meetings, ...
Industry/Entity Type
Consulting
Look and feel

```html
<!DOCTYPE html>
<html lang="en">
<head>
<meta charset="utf-8">
<title>Kelbrook Varga — Conflict Resolution &amp; Performance Consulting</title>
<link rel="stylesheet" href="https://fonts.googleapis.com/css2?family=Gelasio:ital,wght@0,400;0,500;1,400&family=Tinos:wght@400&family=Open+Sans:wght@400&display=swap">
<style>
  :root {
    --page-bg: #f4f3ef;
    --sheet: #ffffff;
    --bar: #231f20;
    --bar-line: #3a3637;
    --nav-text: #b9b5b2;
    --menu-text: #a9a5a2;
    --navy: #082c50;
    --orange: #e77817;
    --ink: #111111;
    --body-text: #6e6a66;
    --rule: #dddad6;
    --photo-frame: #c8c6c2;
  }
  * { box-sizing: border-box; margin: 0; padding: 0; }
  html, body { width: 1200px; height: 1000px; overflow: hidden; }
  body { background: var(--page-bg); font-family: "Gelasio", Georgia, serif; position: relative; }
  a { color: inherit; text-decoration: none; }

  .sheet { position: absolute; left: 162px; top: 28px; width: 918px; height: 972px; background: var(--sheet); border-left: 1px solid #e6e4e0; border-right: 1px solid #e6e4e0; }

  .main-nav { position: absolute; left: 0; top: 0; width: 918px; height: 48px; background: var(--bar); }
  .main-nav a { position: absolute; top: 16px; font-style: italic; font-size: 13.5px; color: var(--nav-text); letter-spacing: -0.5px; white-space: nowrap; }
  .main-nav .is-active::after { content: ""; position: absolute; left: 50%; top: 18px; margin-left: -3px; border: 3px solid transparent; border-bottom-color: #fff; }

  .brand { position: absolute; left: 0; top: 48px; width: 918px; height: 149px; display: flex; align-items: center; justify-content: center; }
  .brand-name { font-family: "Open Sans", Arial, sans-serif; font-size: 50px; font-weight: 400; color: var(--navy); letter-spacing: 1px; }

  .showcase { position: absolute; left: 0; top: 197px; width: 918px; height: 441px; }
  .case-list { position: absolute; left: 0; top: 0; width: 363px; height: 441px; background: var(--bar); list-style: none; }
  .case-list li { height: 55.1px; border-bottom: 2px solid var(--bar-line); display: flex; align-items: center; padding-left: 18px; padding-top: 6px; font-style: italic; font-size: 19px; color: var(--menu-text); }
  .hero-photo { position: absolute; left: 363px; top: 0; width: 555px; height: 441px; background: linear-gradient(90deg, #8e8e8e 0%, #4a4a50 25%, #2e2e34 55%, #3a3c44 80%, #7d8a98 100%); }
  .slide-dots { position: absolute; left: 34px; top: 403px; display: flex; gap: 5px; }
  .slide-dots span { width: 21px; height: 21px; border-radius: 50%; background: #000; }
  .slide-dots .is-current { background: var(--orange); }

  .services { position: absolute; left: 38px; top: 662px; width: 223px; }
  .section-title { font-family: "Tinos", "Times New Roman", serif; font-weight: 400; font-size: 27px; color: var(--ink); padding-left: 2px; padding-bottom: 8px; border-bottom: 1px solid var(--rule); }
  .service { padding-top: 20px; padding-bottom: 13px; border-bottom: 1px solid var(--rule); }
  .service-title { display: flex; align-items: center; gap: 9px; margin-bottom: 8px; }
  .service-icon { width: 17px; height: 17px; }
  .service-title h3 { font-style: italic; font-weight: 400; font-size: 20px; color: var(--ink); border-bottom: 2px solid #9a9794; line-height: 22px; }
  .service p { width: 210px; }
  .service p, .feature p { font-size: 13.2px; line-height: 19.5px; color: var(--body-text); }
  .learn-more { display: inline-flex; align-items: center; gap: 3px; margin-top: 10px; font-style: italic; font-size: 12px; color: var(--ink); }
  .learn-more::after { content: ""; border: 3px solid transparent; border-left: 5px solid var(--orange); border-right: 0; }

  .feature { position: absolute; left: 309px; top: 674px; width: 550px; }
  .team-photo { width: 299px; height: 153px; border: 4px solid var(--photo-frame); background: linear-gradient(90deg, #a88a6a 0%, #c9b596 40%, #b9a282 70%, #8f7458 100%); }
  .quality-claim { position: absolute; left: 327px; top: 34px; font-family: "Tinos", "Times New Roman", serif; font-weight: 400; font-size: 24px; line-height: 30px; color: var(--ink); }
  .feature p { margin-top: 19px; width: 545px; }
</style>
</head>
<body>
  <div class="sheet">
    <nav class="main-nav">
      <a class="is-active" href="#" style="left:16px">Home</a>
      <a href="#" style="left:82px">Services</a>
      <a href="#" style="left:163px">Case studies</a>
      <a href="#" style="left:272px">Engaging us</a>
      <a href="#" style="left:383px">About Conflict &amp; low performance</a>
      <a href="#" style="left:614px">Conflict resolution App</a>
      <a href="#" style="left:785px">About</a>
      <a href="#" style="left:854px">Contact</a>
    </nav>

    <header class="brand">
      <span class="brand-name">KELBROOK VARGA</span>
    </header>

    <section class="showcase">
      <ul class="case-list">
        <li>- Cases</li><li>- Cases</li><li>- Cases</li><li>- Cases</li>
        <li>- Cases</li><li>- Cases</li><li>- Cases</li><li>- Cases</li>
      </ul>
      <div class="hero-photo" role="img" aria-label="Businessman in a dark suit reaching out for a handshake">
        <div class="slide-dots"><span></span><span></span><span></span><span class="is-current"></span></div>
      </div>
    </section>

    <section class="services">
      <h2 class="section-title">Our&nbsp; Services</h2>
      <article class="service">
        <div class="service-title">
          <svg class="service-icon" viewBox="0 0 17 17"><circle cx="8.5" cy="8.5" r="8.5" fill="#e77817"/><path d="M6.5 5 L11 8.5 L6.5 12 Z" fill="#fff"/></svg>
          <h3>Assess</h3>
        </div>
        <p>Porta varisum hendreit mauris Lorem ipsum dolor ametcon seter adipcng elit praesent vestib.</p>
        <a class="learn-more" href="#">Learn More</a>
      </article>
      <article class="service">
        <div class="service-title">
          <svg class="service-icon" viewBox="0 0 17 17"><circle cx="8.5" cy="8.5" r="8.5" fill="#e77817"/><path d="M6.5 5 L11 8.5 L6.5 12 Z" fill="#fff"/></svg>
          <h3>Resolve</h3>
        </div>
        <p>Porta varisum hendreit mauris Lorem ipsum dolor ametcon seter adipcng elit praesent vestib.</p>
        <a class="learn-more" href="#">Learn More</a>
      </article>
    </section>

    <section class="feature">
      <div class="team-photo" role="img" aria-label="Four business people in suits walking together through a bright office lobby"></div>
      <h2 class="quality-claim">We Hold<br>The National Quality<br>Standart.</h2>
      <p>Porta varisum hendreit mauris Lorem ipsum dolor ametcon secteter adipcng elit. Praesent magnis. Montes nascetr mugiat suada odio. Morbi nunc odio, gravida atcursus necin luctus uque duis ultricies pharetra magna. Donec accum san malesuada orci. Donec sit amet eros. Lorem ipsum dolor sit amet, consectetuer adipiscing elit.</p>
      <a class="learn-more" href="#">Learn More</a>
    </section>
  </div>
</body>
</html>
```